Creative Magazine Ad - fusing comfort, culture and cuisine for a food supply company

Hello and welcome to this project!

We need an ad for our company, Kela Supply Co, that is going to be in a magazine read by the Australian Army based in Papua New Guinea.

We want an ad that makes people stop and look. The key message is that even though Papua New Guinea is exotic, the food can be the same (as in Australia). And we want to show off what our company does – supplying great food that caters for all.

Your design should include:

Size:
• 1 page at 15cm height x 19.6cm width
Pictures:
• Our logo – Kela Supply Co – where people can see it
• Pictures or elements that capture the tropical landscape, tribal culture and or essence of Papua New Guinea mixed with pictures of Australian food like barbeque, steaks, pies, roast vegetables etc.
Text to add:
• Title: "Taste of Home in the Tropics: Your Australian Culinary Guide in Papua New Guinea”
• Message: "Our mission is to manufacture and procure a diverse range of high-quality food products, catering to the unique needs of defence camps, and supplying small to large wholesalers, retailers, restaurants, hotels, and caterers throughout Papua New Guinea. We are dedicated to supporting our defence forces with the comforts of home, while serving the broader community with exceptional culinary offerings."
• And our contact details:
+675 314 2691
www.ksv.com.pg
sales@kelasupplyco.com.pg

What we need:
• A graphic for printing for the magazine.
• A digital version to use online.

Thanks again – any questions please ask :)

A Bit About Us
Kela Supply Co Ltd is a 100% PNG-owned and managed business and is proud to be one of the largest food supply companies in the country. Our ability to supply a wide range of premium imported, local and in-house manufactured products from our Butchery and Bakery has contributed to the rock-solid reputation for quality and services that Kela Supply Co now enjoys throughout PNG.

We are proud to also sell our wide range of products through our retail outlets (Tova Grill Haus, Tova Crust Haus and Lute Grill Haus) and our popular Quick Service Restaurants (Reef Stacker and Orb Tart Nook). Our Catering division (Tova Welo Catering) owns a vast array of commercial catering equipment and has experience catering for large-scale events in PNG. We are the only company in Papua New Guinea that has the technology to provide “tamper proof” cold and hot individual meal solutions that can be delivered in temperature-controlled vehicles to locations in Port Moresby but also as a solution to large-scale mining camp catering needs.

```html
<!DOCTYPE html>
<html lang="en">
<head>
<meta charset="utf-8">
<title>Kela Supply Co – Taste of Home in the Tropics</title>
<link href="https://fonts.googleapis.com/css2?family=Barlow+Condensed:wght@600;700;800&family=Barlow+Semi+Condensed:wght@500;700&display=swap" rel="stylesheet">
<style>
  :root {
    --ink-light: #ffffff;
    --ink-soft: rgba(255,255,255,0.88);
    --accent-gold: #f2bb5c;
    --sky: #8fb3c9;
    --foliage: #3c4a2a;
    --foliage-dark: #1f2716;
    --wood: #4a2f18;
    --wood-dark: #140d08;
  }
  * { margin: 0; padding: 0; box-sizing: border-box; }
  html, body {
    width: 1200px; height: 919px; overflow: hidden;
    background: var(--wood-dark);
  }
  .ad-page {
    position: relative;
    width: 1200px; height: 919px;
    overflow: hidden;
    font-family: "Barlow Condensed", sans-serif;
    color: var(--ink-light);
  }
  .hero-photo {
    position: absolute; inset: 0;
    background: linear-gradient(180deg,
      var(--sky) 0%,
      #6d8a7e 12%,
      var(--foliage) 28%,
      var(--foliage-dark) 46%,
      #3a2a18 60%,
      var(--wood) 72%,
      #24160c 86%,
      var(--wood-dark) 100%);
  }
  .brand-mark {
    position: absolute;
    left: 640px; top: 34px;
    display: flex; flex-direction: column; align-items: center;
  }
  .brand-mark__row { display: flex; align-items: center; gap: 10px; }
  .brand-mark__name {
    font-weight: 700; font-size: 32px; letter-spacing: 0.5px;
  }
  .brand-mark__dot {
    width: 16px; height: 16px; border-radius: 50%;
    background: var(--ink-light);
  }
  .brand-mark__tagline {
    margin-top: 2px;
    font-family: "Barlow Semi Condensed", sans-serif;
    font-size: 11px; font-weight: 700; letter-spacing: 0.4px;
  }
  .cert-badge {
    position: absolute; left: 880px; top: 30px;
    width: 26px; height: 26px; border-radius: 50%;
    border: 2px solid var(--ink-light);
  }
  .headline {
    position: absolute; left: 0; right: 0; top: 104px;
    text-align: center; text-transform: uppercase;
    text-shadow: 0 2px 10px rgba(0,0,0,0.35);
  }
  .headline__top {
    display: block;
    font-weight: 800; font-size: 120px; line-height: 0.9;
    letter-spacing: 1px;
  }
  .headline__middle {
    display: flex; align-items: center; justify-content: center;
    gap: 22px; margin-top: 6px;
  }
  .headline__rule { width: 200px; height: 3px; background: var(--ink-light); }
  .headline__in-the {
    font-weight: 700; font-size: 58px; line-height: 1; letter-spacing: 1px;
  }
  .headline__main {
    display: block;
    font-weight: 800; font-size: 240px; line-height: 0.85;
    letter-spacing: 3px;
  }
  .strapline {
    position: absolute; left: 0; right: 0; top: 540px;
    text-align: center; text-transform: uppercase;
    font-family: "Barlow Semi Condensed", sans-serif;
    font-weight: 700; font-size: 28px; line-height: 1.35;
    letter-spacing: 6px;
  }
  .mission {
    position: absolute; left: 170px; right: 170px; top: 650px;
    text-align: center;
    font-family: "Barlow Semi Condensed", sans-serif;
    font-weight: 500; font-size: 17px; line-height: 1.5;
    color: var(--ink-soft);
  }
  .contact-rule {
    position: absolute; left: 190px; right: 190px; top: 790px;
    height: 2px; background: var(--ink-light);
  }
  .contact-bar {
    position: absolute; left: 190px; right: 190px; top: 810px;
    display: flex; justify-content: space-between;
    font-weight: 600; font-size: 24px; letter-spacing: 0.8px;
    color: var(--accent-gold); text-transform: uppercase;
  }
</style>
</head>
<body>
  <main class="ad-page">
    <div class="hero-photo" role="img" aria-label="Grilled steak, sliced medium-rare, on a white plate on a wooden table with tropical palms and a beach sunset behind"></div>

    <div class="brand-mark">
      <div class="brand-mark__row">
        <span class="brand-mark__dot"></span>
        <span class="brand-mark__name">Kela Supply Co</span>
      </div>
      <span class="brand-mark__tagline">“100% PNG Owned &amp; Operated”</span>
    </div>
    <span class="cert-badge" aria-hidden="true"></span>

    <h1 class="headline">
      <span class="headline__top">Taste of Home</span>
      <span class="headline__middle">
        <span class="headline__rule"></span>
        <span class="headline__in-the">In the</span>
        <span class="headline__rule"></span>
      </span>
      <span class="headline__main">Tropics</span>
    </h1>

    <p class="strapline">Your Australian Culinary Guide<br>in Papua New Guinea</p>

    <p class="mission">Our mission is to manufacture and procure a diverse range of high-quality food products, catering to the unique needs of defence camps, and supplying small to large wholesalers, retailers, restaurants, hotels, and caterers throughout Papua New Guinea. We are dedicated to supporting our defence forces with the comforts of home, while serving the broader community with exceptional culinary offerings.</p>

    <div class="contact-rule"></div>
    <div class="contact-bar">
      <span class="contact-bar__phone">+675 314 2691</span>
      <span class="contact-bar__web">www.ksv.com.pg</span>
      <span class="contact-bar__email">sales@kelasupplyco.com.pg</span>
    </div>
  </main>
</body>
</html>
```